Vantoralis 'Private Prism' Book Cover Design project

I need to revise the book cover design I have for my coming book. The design I created through CraftHerd is great but the book has grown and changed so I'm looking for an alternative/option design. I can then choose later from the different options.

I need a book cover that represents the unique book I am creating.

Book Title:
Your True Spectrum

Subtitle: Walking Your Path and Not Your Tag

The book is targeting all readers with a special focus on same sex attracted readers. It should not have stereotypical images.

I am including a file of the book cover I have had designed. The back cover blurb, author info and author pic will remain the same. The colouring of the back cover and spine will, of course, change to match the colouring of the front cover.

The new title will be on the spine and the new title wording.

The front cover will be markedly different using the bold images and rainbow colours of the images found in the files I am uploading for you.

I am thinking of a large boldly coloured rainbow face with the title and subtitle ON the image. The image will be the whole cover. It will fill the cover as much as possible with the text added onto the pic.

The bold pictures I am including will give you the idea of what I'm looking for.

ANY of the images I've uploaded can be used as the actual front cover image OR the designer might have/find some suitable image to be used. The image is to be large and bold and fill the cover. Hopefully a positive energy.
It needs to be eye-catching and striking and bold and positive.

So...the book cover sample file I've provided can keep the back cover with completely new colouring. The front cover is completely new with new image, wording and energy.

It is to be a rainbow coloured face or figure for the cover image.

I hope that is clear enough for you. I'm very happy to discuss and clarify these ideas with the designer. Looking forward to another great CraftHerd experience.

Target Market(s)

Wide audience with special focus on Same Sex Attracted individuals

Font styles to use
Script
Other font styles liked:
• Some form of handwriting font to make the book title and text appear more personal....as if handwritten by me.

Requirements
Must have
• Boldness, Quirky, Rainbow Colour, Image to fill the cover, maybe dark cover contrasting background.
Nice to have
• A well balanced back cover especially in the area where the barcode will be placed.
Should not have
• No stereotypical images

```html
<!DOCTYPE html>
<html lang="en">
<head>
<meta charset="utf-8">
<title>Your True Spectrum – Book Cover</title>
<link rel="stylesheet" href="https://fonts.googleapis.com/css2?family=Amatic+SC:wght@700&family=Damion&family=Kalam:wght@300;400&family=Libre+Baskerville:ital@0;1&family=Montserrat:wght@400;600;800&display=swap">
<style>
  :root {
    --ink: #141414;
    --spine: #232323;
    --paper: #f2f2f2;
    --sky: #1fa6de;
    --teal: #4fc1c4;
    --lime: #b3c43b;
    --pink: #e0458f;
    --orange: #e0862a;
    --blue: #1f9fdc;
    --brush: #d47e2c;
  }
  * { box-sizing: border-box; margin: 0; padding: 0; }
  html, body { width: 1200px; height: 876px; overflow: hidden; background: var(--ink); }
  .cover { position: relative; width: 1200px; height: 876px; overflow: hidden; color: var(--paper); }

  /* back cover */
  .back { position: absolute; left: 0; top: 0; width: 565px; height: 876px;
    background: radial-gradient(ellipse at 40% 45%, #3a3228 0%, #1d1a17 55%, #121212 100%); }
  .colour-bar { position: absolute; left: 0; width: 565px; height: 5px; }
  .colour-bar.top { top: 0; } .colour-bar.bottom { bottom: 0; }
  .colour-bar span { position: absolute; top: 0; height: 5px; width: 95px; }
  .colour-bar span:nth-child(1) { left: 37px; background: var(--teal); }
  .colour-bar span:nth-child(2) { left: 137px; background: var(--lime); }
  .colour-bar span:nth-child(3) { left: 242px; background: var(--pink); }
  .colour-bar span:nth-child(4) { left: 342px; background: var(--orange); }
  .colour-bar span:nth-child(5) { left: 446px; background: var(--blue); }

  .pull-quote { position: absolute; left: 22px; top: 22px; width: 521px; text-align: center;
    font-family: "Amatic SC", cursive; font-weight: 700; font-size: 27px; line-height: 35px; }
  .tagline { position: absolute; left: 0; top: 139px; width: 565px; text-align: center;
    font-family: "Montserrat", sans-serif; font-weight: 800; font-size: 14.5px; color: var(--sky); }
  .tagline-sub { position: absolute; left: 0; top: 161px; width: 565px; text-align: center;
    font-family: "Libre Baskerville", serif; font-size: 13.5px; }
  .blurb { position: absolute; left: 22px; top: 200px; width: 521px; text-align: center;
    font-family: "Libre Baskerville", serif; font-size: 12.6px; line-height: 22.5px; }
  .brush-band { position: absolute; left: 0; top: 392px; width: 565px; height: 130px; }
  .brush-quote { position: absolute; left: 55px; top: 416px; width: 455px; text-align: center;
    font-family: "Libre Baskerville", serif; font-style: italic; font-size: 13.5px; line-height: 22.3px; }
  .closing { position: absolute; left: 28px; top: 537px; width: 509px; text-align: center;
    font-family: "Libre Baskerville", serif; font-size: 13.4px; line-height: 23px; }
  .author-photo { position: absolute; left: 29px; top: 628px; width: 136px; height: 136px; border-radius: 50%;
    background: linear-gradient(180deg, #7f9a63 0%, #a7a08a 40%, #b24f93 62%, #6f4a78 100%); }
  .author-bio { position: absolute; left: 182px; top: 628px; width: 370px;
    font-family: "Montserrat", sans-serif; font-size: 11px; line-height: 21.5px; }
  .author-bio .name { font-weight: 800; font-size: 14px; line-height: 20px; margin-bottom: 4px; }
  .mark-box { position: absolute; background: #000; border: 1px solid #3a3a3a;
    display: flex; align-items: center; justify-content: center;
    font-family: "Montserrat", sans-serif; font-size: 12px; }
  .mark-box.publisher { left: 29px; top: 779px; width: 154px; height: 70px; }
  .mark-box.partner { left: 190px; top: 779px; width: 153px; height: 70px; }
  .mark-box.isbn { left: 360px; top: 742px; width: 183px; height: 107px; align-items: flex-start; padding-top: 52px; }

  /* spine */
  .spine { position: absolute; left: 565px; top: 0; width: 53px; height: 876px; background: var(--spine); }
  .spine-title { position: absolute; left: 6px; top: 30px; writing-mode: vertical-rl;
    font-family: "Damion", cursive; font-size: 38px; line-height: 42px; letter-spacing: 2px; }
  .spine-author { position: absolute; left: 11px; top: 670px; writing-mode: vertical-rl;
    font-family: "Kalam", cursive; font-weight: 300; font-size: 23px; line-height: 30px; letter-spacing: 3px; }

  /* front cover: full-bleed image with overlaid type */
  .front { position: absolute; left: 618px; top: 0; width: 582px; height: 876px; background: var(--ink); }
  .cover-art { position: absolute; inset: 0;
    background:
      linear-gradient(180deg, rgba(10,10,10,0) 52%, rgba(10,10,10,0.55) 68%, rgba(10,10,10,0.6) 88%, rgba(10,10,10,0.2) 100%),
      radial-gradient(ellipse 40% 30% at 30% 78%, #d8a230 0%, rgba(216,162,48,0) 100%),
      radial-gradient(ellipse 35% 30% at 80% 70%, #2c7a3c 0%, rgba(44,122,60,0) 100%),
      radial-gradient(ellipse 40% 35% at 20% 30%, #c43f86 0%, rgba(196,63,134,0) 100%),
      radial-gradient(ellipse 45% 35% at 75% 25%, #1f6fb0 0%, rgba(31,111,176,0) 100%),
      radial-gradient(ellipse 55% 40% at 48% 45%, #c9532f 0%, #7d3a74 45%, #1a1a1a 100%); }
  .title { position: absolute; left: 0; top: 584px; width: 582px; text-align: center;
    font-family: "Damion", cursive; font-weight: 400; font-size: 66px; line-height: 90px; white-space: nowrap;
    text-shadow: 0 2px 8px rgba(0,0,0,0.6); }
  .subtitle { position: absolute; left: 0; top: 680px; width: 582px; text-align: center;
    font-family: "Kalam", cursive; font-weight: 300; font-size: 25px; letter-spacing: 1.6px;
    text-shadow: 0 1px 6px rgba(0,0,0,0.7); }
  .author { position: absolute; left: 0; top: 734px; width: 582px; text-align: center;
    font-family: "Kalam", cursive; font-weight: 300; font-size: 33px; letter-spacing: 4px;
    text-shadow: 0 1px 6px rgba(0,0,0,0.7); }
</style>
</head>
<body>
<div class="cover">

  <section class="back">
    <div class="colour-bar top"><span></span><span></span><span></span><span></span><span></span></div>

    <p class="pull-quote">“It’s important to challenge our accepted beliefs and the stories we tell ourselves individually and as a community, if there is to be any sense of wholeness, happiness and future.”</p>

    <p class="tagline">YOUR SPECTRUM IS MUCH MORE THAN THE FLAG YOU WAVE.</p>
    <p class="tagline-sub">It is the unique and individual YOU behind the layers, labels and stories</p>

    <p class="blurb">This first book by Liam Dorsey asks each of us to consider our accepted beliefs and personal stories as we explore the possible ways to WALK OUR PATH AND NOT A TAG. Doing this requires some honest inner work and a journey that will need to be passionately personal and authentically individual.<br>‘Your True Spectrum’ reminds us that a beautiful, rainbow life is more than sexuality, personality or gender or having a camp, team or tribe to belong to. It is much more than any acronym, scene or lifestyle. It’s ‘an inside job’, deeply heartfelt and courageously unique. Finding and living the YOU of YOU has boldness and power and magic in it.</p>

    <svg class="brush-band" viewBox="0 0 565 130" preserveAspectRatio="none" aria-hidden="true">
      <path d="M0 14 L60 8 L140 12 L230 4 L330 10 L420 6 L500 12 L565 8 L565 118 L480 124 L390 116 L300 126 L200 118 L110 125 L40 116 L0 122 Z" fill="var(--brush)"/>
    </svg>
    <p class="brush-quote">"Living a meaningful, happy existence is about being true to the whole, complex, integrated person that you are and being strong enough and aware enough and reflective enough to know yourself, love yourself and be yourself" Liam Dorsey</p>

    <p class="closing">This simple and insightful book will help you explore ways to bravely and honestly know, love and be yourself no matter what the rest of the world might be doing or saying or expecting.</p>

    <div class="author-photo" role="img" aria-label="Portrait photo of the author"></div>
    <div class="author-bio">
      <p class="name">Liam Dorsey</p>
      <p>Personal Change coach and Educator<br>VANTORALIS Coaching and wellness<br>Advocate, Activist, Writer and Support For MEN<br>WHO DATE MEN and their wholeness<br>happiness and human Rights</p>
    </div>

    <div class="mark-box publisher">Publisher Logo 1</div>
    <div class="mark-box partner">Another logo</div>
    <div class="mark-box isbn">ISBN / Barcode</div>

    <div class="colour-bar bottom"><span></span><span></span><span></span><span></span><span></span></div>
  </section>

  <section class="spine">
    <p class="spine-title">Your True Spectrum</p>
    <p class="spine-author">Liam Dorsey</p>
  </section>

  <section class="front">
    <div class="cover-art" role="img" aria-label="Full-cover photo of a figure covered in bold rainbow body paint against a black background"></div>
    <h1 class="title">Your True Spectrum</h1>
    <p class="subtitle">Walking Your Path and Not Your Tag</p>
    <p class="author">Liam Dorsey</p>
  </section>

</div>
</body>
</html>
```